Orvik Lines website

i'm looking for a promotional website for my business.
we provide Rope Access, Work at Height & Difficult Access services.
we treat water leak into buildings, external renovation of buildings, windows cleaning, confined spaces services and practically jobs in which the access is difficult.
here are examples of web site i like :
http://www.layoutbazaar.example/wordpress-themes/51872.html
http://www.layoutbazaar.example/joomla-templates/51294.html

private people, commercial household chiefs, maintenance managers

Business

• - mobile friendly
- frindlo redirection
- 5 tabs
- one more customizable page - so i can add a photo and a description of the service corresponding (for now i offer 7 different services)
- contact us on each page with no redirection
- we are offering 7 different services
the website will be published in Israel which means right to left or centered for english option in the future. (logo on left hand corner)

- no flash
- should be future customisable - for future
• - a space for a slogan
- non scrollable
- photos on the landing page + redirection to gallery (photos and short films)
- 3 dynamic banners with short description of the theme of each, clicking on the banner after it opened will redirect to it's corresponding page.

```html
<!DOCTYPE html>
<html lang="en">
<head>
<meta charset="utf-8">
<title>Orvik Lines – Services</title>
<link rel="stylesheet" href="https://fonts.googleapis.com/css2?family=Montserrat:wght@400;500&family=Oswald:wght@500&display=swap">
<style>
  :root {
    --bg-page: #262626;
    --bg-header: #383838;
    --bg-footer: #1b1b1b;
    --nav-active: #0c0c0c;
    --text-main: #c9c9c9;
    --text-light: #ffffff;
    --text-muted: #a9a9a9;
    --rule: #4a4a4a;
    --social-a: #3b5a9a;
    --social-b: #35a7d8;
    --social-c: #1f7ab3;
  }
  html, body {
    margin: 0;
    padding: 0;
    width: 1200px;
    height: 1013px;
    overflow: hidden;
    background: var(--bg-page);
  }
  .site {
    position: relative;
    width: 1200px;
    height: 1013px;
    background: var(--bg-page);
    font-family: "Montserrat", Arial, sans-serif;
    color: var(--text-main);
    overflow: hidden;
  }
  .site-header {
    position: absolute;
    left: 0; top: 0;
    width: 1200px; height: 90px;
    background: var(--bg-header);
  }
  .hero {
    position: absolute;
    left: 0; top: 0;
    width: 1200px; height: 560px;
  }
  .brand-badge {
    position: absolute;
    left: 138px; top: -72px;
    width: 192px; height: 192px;
    border-radius: 50%;
    background: var(--text-light);
  }
  .brand-name {
    position: absolute;
    left: 342px; top: 16px;
    margin: 0;
    font-family: "Oswald", "Arial Narrow", sans-serif;
    font-weight: 500;
    font-size: 27px;
    letter-spacing: 0.2px;
    color: var(--text-light);
    text-transform: uppercase;
  }
  .main-nav {
    position: absolute;
    top: 0; right: 144px;
    display: flex;
    margin: 0; padding: 0;
    list-style: none;
  }
  .main-nav a {
    display: block;
    height: 78px;
    line-height: 72px;
    padding: 0 12px;
    font-size: 17.5px;
    font-weight: 500;
    color: var(--text-light);
    text-decoration: none;
    text-transform: uppercase;
    letter-spacing: 0.4px;
  }
  .main-nav .is-active a { background: var(--nav-active); }
  .content {
    position: absolute;
    left: 151px; top: 548px;
    width: 903px;
  }
  .content h1 {
    margin: 0;
    padding-bottom: 10px;
    font-size: 24px;
    font-weight: 500;
    color: var(--text-light);
    border-bottom: 1px dotted var(--rule);
  }
  .content p {
    margin: 14px 0 18px;
    font-size: 14.3px;
    line-height: 18.8px;
    color: var(--text-main);
  }
  .service-list {
    margin: 0; padding: 0;
    list-style: none;
  }
  .service-list li {
    position: relative;
    padding-left: 14px;
    height: 28.2px;
    font-size: 14.3px;
    line-height: 18px;
    color: var(--text-main);
  }
  .service-list li::before {
    content: "";
    position: absolute;
    left: 0; top: 5px;
    border-left: 4px solid var(--text-light);
    border-top: 3.5px solid transparent;
    border-bottom: 3.5px solid transparent;
  }
  .site-footer {
    position: absolute;
    left: 0; top: 920px;
    width: 1200px; height: 93px;
  }
  .footer-meta {
    position: absolute;
    left: 151px; top: 57px;
    margin: 0;
    font-size: 13.5px;
    color: var(--text-muted);
    text-transform: uppercase;
  }
  .footer-social {
    position: absolute;
    right: 147px; top: 50px;
    display: flex;
    align-items: center;
    gap: 6px;
  }
  .footer-social .label {
    font-size: 13.5px;
    font-weight: 500;
    color: var(--text-light);
    text-transform: uppercase;
    margin-right: 4px;
  }
  .social-chip {
    display: block;
    width: 29px; height: 29px;
    border-radius: 3px;
  }
  .social-chip.frindlo { background: var(--social-a); }
  .social-chip.chirpio { background: var(--social-b); }
  .social-chip.lynkwork { background: var(--social-c); }
</style>
</head>
<body>
<div class="site">
  <div class="site-header"></div>

  <svg class="hero" viewBox="0 0 1200 560" role="img" aria-label="Photo: rope access technician working on a rooftop edge beside a cable-stayed bridge, city skyline in the haze behind">
    <defs>
      <linearGradient id="heroTone" x1="0" y1="0" x2="0" y2="1">
        <stop offset="0" stop-color="#c9bfc3"/>
        <stop offset="0.35" stop-color="#b8aca8"/>
        <stop offset="0.6" stop-color="#9a8e84"/>
        <stop offset="0.85" stop-color="#c4b2a0"/>
        <stop offset="1" stop-color="#8d7e70"/>
      </linearGradient>
    </defs>
    <polygon points="0,66 1200,86 1200,474 0,542" fill="url(#heroTone)"/>
  </svg>

  <div class="brand-badge"></div>
  <p class="brand-name">Orvik Lines</p>

  <ul class="main-nav">
    <li><a href="#">Home</a></li>
    <li class="is-active"><a href="#">Services</a></li>
    <li><a href="#">Projects</a></li>
    <li><a href="#">Gallery</a></li>
    <li><a href="#">Contact Us</a></li>
  </ul>

  <main class="content">
    <h1>Services</h1>
    <p>Lorem ipsum dolor sit amet, consectetur adipisicing elit, sed do eiusmod tempor incididunt ut labore et dolore magna aliqua. Ut enim ad minim veniam, quis nostrud exercitation ullamco laboris nisi ut aliquip ex ea commodo consequat. Duis aute irure dolor in reprehenderit in voluptate velit esse cillum dolore eu fugiat nulla pariatur. Excepteur sint occaecat cupidatat non proident, sunt in culpa qui officia deserunt mollit anim id est laborum.</p>
    <ul class="service-list">
      <li>Work at Height &amp; Difficult Access services.</li>
      <li>We treat water leak into buildings,</li>
      <li>External renovation of buildings,</li>
      <li>Windows cleaning,</li>
      <li>Private people</li>
      <li>Commercial household chiefs</li>
      <li>Maintenance managers</li>
    </ul>
  </main>

  <footer class="site-footer">
    <svg width="1200" height="93" viewBox="0 0 1200 93" style="position:absolute;left:0;top:0">
      <polygon points="0,4 1200,40 1200,93 0,93" fill="var(--bg-footer)"/>
    </svg>
    <p class="footer-meta">Orvik Lines © 2013 &nbsp;|&nbsp; Privacy Policy</p>
    <div class="footer-social">
      <span class="label">Connect with us</span>
      <a class="social-chip frindlo" href="#" aria-label="Frindlo"></a>
      <a class="social-chip chirpio" href="#" aria-label="Chirpio"></a>
      <a class="social-chip lynkwork" href="#" aria-label="Lynkwork"></a>
    </div>
  </footer>
</div>
</body>
</html>
```